Personal Tax Specialists Banner

We need banner adverts for a personal tax firm. We specialise in Luxembourg, US and UK personal taxation. The banner should be modern, cool, simple and illustrated.

Banner should highlight "Personal Taxation Specialists" and the countries that we specialise in, "Luxembourg", "US" and "UK".

Target Market(s)

Individuals looking for assistance with tax return preparation.

Industry/Entity Type

Finance And Accounting

Colors

Designer to choose colors to be used in the design.

Requirements
Must have
• Output in GIF.
• The main banner size is 980 x 120 and some smaller square banners (300 x 300)
• Button to link back to website www.quendrifin.com
Nice to have
• We would like an illustrated design if possible.

```html
<!DOCTYPE html>
<html lang="en">
<head>
<meta charset="utf-8">
<title>Quendri Tax &amp; Consulting – Banner Set</title>
<link rel="stylesheet" href="https://fonts.googleapis.com/css2?family=Roboto:wght@400;500&display=swap">
<style>
  :root{
    --maroon:#7b2540;
    --rose:#bf9aa3;
    --grey:#808184;
    --grey-mid:#b1b1b3;
    --grey-light:#e6e7e8;
    --frame:#999a9c;
    --white:#ffffff;
    --font:"Roboto", Arial, sans-serif;
  }
  *{box-sizing:border-box;margin:0;padding:0}
  html,body{width:1200px;height:355px;overflow:hidden;background:var(--white)}
  .canvas{position:relative;width:1200px;height:355px;font-family:var(--font);overflow:hidden}
  .shapes{position:absolute;left:0;top:0}

  /* square banner set */
  .square-set{position:absolute;left:346px;top:0;width:484px;height:166px;background:var(--grey-light);border:1px solid var(--frame)}
  .square{position:absolute;top:13px;width:138px;height:137px;border:1px solid var(--frame);background:var(--white);overflow:hidden}
  .square svg{position:absolute;left:0;top:0}
  .square--one{left:17px}
  .square--two{left:173px}
  .square--three{left:329px}
  .brand-small{position:absolute;display:flex;align-items:center;gap:4px}
  .brand-small__ring{width:20px;height:20px;border-radius:50%;border:1.5px solid var(--grey)}
  .brand-small__name{font-size:13px;line-height:1;color:var(--maroon);letter-spacing:.3px}
  .brand-small__tag{font-size:5px;line-height:1;color:var(--grey);margin-top:2px;letter-spacing:.2px}
  .site-small{position:absolute;font-size:7px;color:var(--maroon);white-space:nowrap}

  /* main banner */
  .brand-ring{position:absolute;left:168px;top:204px;width:136px;height:136px;border-radius:50%;border:4px solid var(--grey)}
  .brand-name{position:absolute;left:432px;top:206px;font-size:82px;line-height:1;color:var(--maroon);letter-spacing:1px;white-space:nowrap}
  .brand-tag{position:absolute;left:790px;top:232px;font-size:22px;line-height:1.2;color:var(--grey);letter-spacing:.5px;white-space:nowrap}
  .specialism{position:absolute;left:436px;top:291px;font-size:11px;line-height:13px;font-weight:500;letter-spacing:1.6px;color:var(--grey);white-space:nowrap}
  .specialism__countries{color:var(--maroon)}
  .site-button{position:absolute;left:470px;top:311px;width:300px;text-align:center;font-size:27px;line-height:34px;color:var(--white);text-decoration:none;white-space:nowrap}
</style>
</head>
<body>
<div class="canvas">

  <!-- square banners -->
  <div class="square-set">
    <div class="square square--one">
      <svg width="138" height="137" viewBox="0 0 138 137">
        <rect width="138" height="137" fill="var(--grey-light)"/>
        <polygon points="112,0 138,0 138,137 42,137" fill="var(--white)"/>
        <polygon points="68,2 108,2 56,86 12,86" fill="var(--rose)"/>
        <polygon points="44,12 82,12 42,70 20,70" fill="none" stroke="var(--white)" stroke-width="1.2"/>
        <path d="M92,77 l4,3 l4,-3 M92,81 l4,3 l4,-3 M92,85 l4,3 l4,-3" fill="none" stroke="var(--maroon)" stroke-width="1.4"/>
      </svg>
      <span class="site-small" style="right:6px;top:92px">www.quendrifin.com</span>
      <div class="brand-small" style="left:50px;top:110px">
        <span class="brand-small__ring"></span>
        <div><div class="brand-small__name">QUENDRI</div><div class="brand-small__tag">TAX &amp; CONSULTING</div></div>
      </div>
    </div>

    <div class="square square--two">
      <svg width="138" height="137" viewBox="0 0 138 137">
        <polygon points="138,38 138,137 30,137" fill="var(--grey-light)"/>
        <polygon points="138,30 138,46 8,112 8,96" fill="var(--maroon)"/>
        <polygon points="138,50 138,56 40,106 40,100" fill="none" stroke="var(--white)" stroke-width="1.2"/>
        <path d="M40,66 l4,-3 l4,3 M40,70 l4,-3 l4,3 M40,74 l4,-3 l4,3" fill="none" stroke="var(--maroon)" stroke-width="1.4"/>
      </svg>
      <div class="brand-small" style="left:12px;top:14px">
        <span class="brand-small__ring"></span>
        <div><div class="brand-small__name">QUENDRI</div><div class="brand-small__tag">TAX &amp; CONSULTING</div></div>
      </div>
      <span class="site-small" style="left:10px;top:48px">www.quendrifin.com</span>
    </div>

    <div class="square square--three">
      <svg width="138" height="137" viewBox="0 0 138 137">
        <polygon points="76,0 138,0 138,137" fill="var(--grey-light)"/>
        <polygon points="92,56 116,56 98,82 72,82" fill="var(--grey-mid)"/>
        <polygon points="70,98 98,98 72,137 44,137" fill="var(--grey-mid)"/>
        <polygon points="82,86 112,86 82,132 54,132" fill="none" stroke="var(--white)" stroke-width="1.2"/>
        <path d="M32,48 l4,3 l4,-3 M32,52 l4,3 l4,-3 M32,56 l4,3 l4,-3" fill="none" stroke="var(--maroon)" stroke-width="1.4"/>
      </svg>
      <div class="brand-small" style="left:6px;top:14px">
        <span class="brand-small__ring"></span>
        <div><div class="brand-small__name">QUENDRI</div><div class="brand-small__tag">TAX &amp; CONSULTING</div></div>
      </div>
      <span class="site-small" style="left:4px;top:64px">www.quendrifin.com</span>
    </div>
  </div>

  <!-- main banner shapes -->
  <svg class="shapes" width="1200" height="355" viewBox="0 0 1200 355">
    <polygon points="80,195 996,195 948,306 80,306" fill="var(--white)"/>
    <polygon points="62,314 150,314 136,345 56,345" fill="var(--maroon)"/>
    <polygon points="130,308 948,308 930,355 104,355" fill="var(--grey)"/>
    <polygon points="30,195 122,195 64,262 122,330 30,330 0,300 0,226" fill="var(--grey)"/>
    <polyline points="132,200 72,262 132,324" fill="none" stroke="var(--grey)" stroke-width="4"/>
    <polygon points="306,195 376,195 420,262 374,306 306,306 358,262" fill="var(--grey)"/>
    <polyline points="300,202 350,262 300,300" fill="none" stroke="var(--grey)" stroke-width="4"/>
    <polygon points="1008,195 1128,195 1068,332 948,332" fill="var(--maroon)"/>
    <polygon points="1132,195 1200,195 1172,276 1104,276" fill="var(--maroon)"/>
    <path d="M826,322 l-8,10 l8,10 M838,322 l-8,10 l8,10 M850,322 l-8,10 l8,10" fill="none" stroke="var(--white)" stroke-width="3"/>
  </svg>

  <span class="brand-ring"></span>
  <div class="brand-name">QUENDRI</div>
  <div class="brand-tag">TAX &amp;<br>CONSULTING</div>
  <p class="specialism">PERSONAL TAXATION SPECIALISTS <span class="specialism__countries">· LUXEMBOURG · US · UK</span></p>
  <a class="site-button" href="#">www.quendrifin.com</a>
</div>
</body>
</html>
```